Harrow's Electrical & Solar - Business Cards

I want my business card to stand out from the rest. I will provide my business name logo and my icon logo to be implemented onto the card.

On the front of the card, can i have the following. Just make it neat & professional please.

Liam Corbett
harrowselectrical@quillmail.test
0438 917 605
ABN: 41 602 719 384
License No. 582164K
FREE QUOTES
24/7 Emergency

On the back of the card, can I have "Our Services" and maybe add the S logo on the back in the background or something. Under "Our Services" I want the following:

LED Lighting Upgrades
Switches & Outlets
Smoke Alarms
Switchboard Upgrades
Fault Finding
Rewiring
New Builds
Test & Tagging
All Electrical Maintenance & Repairs

Can you guys add the instagram logo and next to it, put harrows_electrical

Can you guys also add the facebook logo and next to it put Harrow's Electrical & Solar. Make sure the instagram & facebook icon is in either white, green or black.

Also I have put down double sided, not sure why when i save it, it keeps going to single sided. I need my business card double sided.

Target Market(s)

New Customers

Contact Information for Business Card

Liam Corbett harrowselectrical@quillmail.test 0438 917 605 ABN: 41 602 719 384 License No. 582164K FREE QUOTES 24/7 Emergency

Requirements
Must have
• must be tidy, professional and appealing

```html
<!DOCTYPE html>
<html lang="en">
<head>
<meta charset="utf-8">
<title>Harrow's Electrical &amp; Solar – Business Cards</title>
<link rel="stylesheet" href="https://fonts.googleapis.com/css2?family=Poppins:wght@400;500;600&family=Russo+One&display=swap">
<style>
  :root{
    --bg:#2b2623;
    --card:#1c1c1d;
    --green:#2fd24f;
    --green-dark:#1f9e37;
    --silver:#c9ccd1;
    --white:#f2f2f2;
  }
  *{box-sizing:border-box;margin:0;padding:0}
  html,body{width:1200px;height:842px;overflow:hidden;background:var(--bg)}
  body{position:relative;font-family:"Poppins",sans-serif;color:var(--white)}
  .card{position:absolute;top:261px;width:550px;height:320px;background:var(--card);overflow:hidden;box-shadow:0 14px 30px rgba(0,0,0,.55)}
  .card--front{left:33px}
  .card--back{left:617px}

  /* front */
  .band{position:absolute;left:0;right:0;height:12px;background:linear-gradient(90deg,var(--green-dark),var(--green))}
  .band--top{top:18px}
  .band--bottom{bottom:18px}
  .brand{position:absolute;top:52px;left:0;right:0;display:flex;justify-content:center;align-items:center;gap:14px}
  .brand__mark{width:58px;height:58px;border-radius:50%;border:4px solid var(--green)}
  .brand__name{font-family:"Russo One",sans-serif;font-size:30px;color:var(--silver);letter-spacing:1px}
  .holder{position:absolute;top:128px;left:0;right:0;text-align:center;font-family:"Russo One",sans-serif;font-size:24px;color:var(--green);letter-spacing:1px}
  .details{position:absolute;top:170px;left:0;right:0;display:flex;justify-content:center;gap:18px}
  .contact{text-align:right;font-size:15px;line-height:24px}
  .contact span{display:inline-flex;align-items:center;gap:8px}
  .contact svg{width:14px;height:14px}
  .divider{width:1px;background:var(--green-dark)}
  .legal{font-size:14px;line-height:24px;color:var(--green)}
  .rule{position:absolute;left:24px;right:24px;top:245px;height:1px;background:var(--green-dark)}
  .offer{position:absolute;top:233px;left:50%;transform:translateX(-50%);background:var(--card);padding:0 12px;font-size:15px;white-space:nowrap}
  .offer strong{font-family:"Russo One",sans-serif;font-weight:400;color:var(--green)}

  /* back */
  .side-bar{position:absolute;width:22px;height:88px;background:linear-gradient(180deg,var(--green),var(--green-dark))}
  .side-bar::after{content:"";position:absolute;top:0;bottom:0;width:4px;background:var(--silver)}
  .side-bar--left{left:0;top:160px}
  .side-bar--left::after{right:-8px}
  .side-bar--right{right:0;top:50px}
  .side-bar--right::after{left:-8px}
  .watermark{position:absolute;left:175px;top:50px;width:210px;height:210px;border-radius:50%;border:14px solid rgba(255,255,255,.035)}
  .services-title{position:absolute;top:44px;left:0;right:0;text-align:center;font-family:"Russo One",sans-serif;font-size:26px;color:var(--green);letter-spacing:1px}
  .services{position:absolute;top:98px;left:72px;right:50px;display:flex;gap:34px}
  .services ul{list-style:none;font-size:14px;line-height:25px}
  .services li{position:relative;padding-left:14px}
  .services li::before{content:"";position:absolute;left:0;top:8px;border-left:5px solid var(--green);border-top:4px solid transparent;border-bottom:4px solid transparent;transform:rotate(-30deg)}
  .socials{position:absolute;bottom:34px;left:60px;right:40px;display:flex;justify-content:space-between;font-size:15px}
  .social{display:flex;align-items:center;gap:10px}
  .social__dot{width:24px;height:24px;border-radius:50%;border:2px solid var(--green)}
</style>
</head>
<body>
  <section class="card card--front">
    <div class="band band--top"></div>
    <div class="brand">
      <div class="brand__mark"></div>
      <div class="brand__name">HARROW'S ELECTRICAL &amp; SOLAR</div>
    </div>
    <div class="holder">LIAM CORBETT</div>
    <div class="details">
      <div class="contact">
        <span>0438 917 605
          <svg viewBox="0 0 24 24" fill="none" stroke="#2fd24f" stroke-width="2.4"><path d="M5 3h4l2 5-3 2a12 12 0 0 0 6 6l2-3 5 2v4a2 2 0 0 1-2 2A18 18 0 0 1 3 5a2 2 0 0 1 2-2z"/></svg>
        </span><br>
        <span>harrowselectrical@quillmail.test
          <svg viewBox="0 0 24 24" fill="none" stroke="#2fd24f" stroke-width="2.4"><rect x="2" y="5" width="20" height="14"/><path d="M2 5l10 8 10-8"/></svg>
        </span>
      </div>
      <div class="divider"></div>
      <div class="legal">ABN: 41 602 719 384<br>License No. 582164K</div>
    </div>
    <div class="rule"></div>
    <div class="offer">FREE QUOTES &nbsp;|&nbsp; <strong>24/7 EMERGENCY</strong></div>
    <div class="band band--bottom"></div>
  </section>

  <section class="card card--back">
    <div class="watermark" role="img" aria-label="Faint brand mark in the background"></div>
    <div class="side-bar side-bar--left"></div>
    <div class="side-bar side-bar--right"></div>
    <h2 class="services-title">OUR SERVICES</h2>
    <div class="services">
      <ul>
        <li>LED Lighting Upgrades</li>
        <li>Switches &amp; Outlets</li>
        <li>Smoke Alarms</li>
        <li>Switchboard Upgrades</li>
        <li>Fault Finding</li>
      </ul>
      <ul>
        <li>Rewiring</li>
        <li>New Builds</li>
        <li>Test &amp; Tagging</li>
        <li>All Electrical Maintenance<br>&amp; Repairs</li>
      </ul>
    </div>
    <div class="socials">
      <div class="social"><span class="social__dot"></span>harrows_electrical</div>
      <div class="social"><span class="social__dot"></span>Harrow's Electrical &amp; Solar</div>
    </div>
  </section>
</body>
</html>
```